Business Card design for a skin clinic

i would like a business card design for our skin clinic.
our logo colors are Blue and Grey and Bule /white.
we are searching for a minimalistic design yet very elegant,dynamic and professional which can reflect a professional medical skin care clinic( not a beauty salon).
THE DESGIN IS NOT FOR A PERSON IT WILL BE USED IN THE CLINIC FOR CLIENTS SO THERE SHOULD BE NO NAME OF A PERSON ONLY THE CLINIC NAME AND THE CONTACT INFO

Target Market(s)
young and old womens
Industry/Entity Type
Business
Contact Information for Business Card
we have 2 address and both should be on the card.
address A: Lindenhoflaan 214B, 3041KP Rotterdam, Tel 010 483 21 95
address B: Zonnewijzerstraat 238, 1062RT Amsterdam Tel 020 571 3829
website www.huidpuntzorg.nu, email info@huidpuntzorg.nu
Look and feel
Each slider illustrates characteristics of the customer's brand and the style your logo design should communicate.

```html
<!DOCTYPE html>
<html lang="nl">
<head>
<meta charset="utf-8">
<title>Huidpuntzorg – Visitekaartje</title>
<link rel="stylesheet" href="https://fonts.googleapis.com/css2?family=Montserrat:wght@400;500;700&family=Lato:wght@400;700&display=swap">
<style>
  :root {
    --bg: #eef0f2;
    --paper: #f7f7f6;
    --blue: #2394d6;
    --blue-dark: #1d84c4;
    --ink: #2a2b2d;
    --ink-soft: #353638;
    --grey: #6c6e70;
    --white: #ffffff;
  }
  * { margin: 0; padding: 0; box-sizing: border-box; }
  html, body { width: 1200px; height: 800px; overflow: hidden; background: var(--bg); }
  body { position: relative; font-family: "Lato", sans-serif; }

  .card {
    position: absolute;
    width: 560px; height: 320px;
    background: var(--paper);
    overflow: hidden;
    box-shadow: 0 6px 18px rgba(0,0,0,0.12);
  }
  .card--front { left: 20px; top: 240px; }
  .card--back  { left: 620px; top: 240px; }

  /* Front */
  .front__topband { position: absolute; left: 0; top: 0; width: 100%; height: 44px; background: var(--ink); }
  .front__topband-segment { position: absolute; top: 0; height: 100%; background: var(--ink-soft); }
  .front__bottomband { position: absolute; left: 0; top: 238px; width: 100%; height: 34px; background: var(--blue); }
  .front__bottomband-segment { position: absolute; top: 0; height: 100%; background: var(--blue-dark); }
  .brand {
    position: absolute; left: 0; top: 104px; width: 100%;
    display: flex; flex-direction: column; align-items: center;
  }
  .brand__row { display: flex; align-items: center; gap: 12px; }
  .brand__mark { width: 18px; height: 18px; background: var(--blue); }
  .brand__name {
    font-family: "Montserrat", sans-serif; font-weight: 500;
    font-size: 34px; letter-spacing: 5px; color: var(--blue);
  }
  .brand__tagline {
    margin-top: 6px;
    font-family: "Montserrat", sans-serif; font-size: 12px;
    letter-spacing: 2.4px; color: var(--grey);
  }

  /* Back */
  .back__side { position: absolute; left: 0; top: 0; width: 180px; height: 100%; background: var(--paper); }
  .back__side .brand {
    top: 50%; left: 50%; width: 320px;
    transform: translate(-50%, -50%) rotate(-90deg);
  }
  .back__side .brand__name { font-size: 25px; letter-spacing: 3px; }
  .back__side .brand__mark { width: 14px; height: 14px; }
  .back__side .brand__tagline { font-size: 10px; letter-spacing: 1.8px; }

  .back__frame { position: absolute; left: 180px; top: 0; right: 0; bottom: 0; background: var(--blue); }
  .back__frame-segment { position: absolute; background: var(--blue-dark); }
  .back__strip { position: absolute; left: 180px; top: 0; width: 52px; height: 100%; }
  .strip__text {
    position: absolute; left: 50%; top: 50%;
    transform: translate(-50%, -50%) rotate(-90deg);
    white-space: nowrap; text-align: center; color: var(--white);
  }
  .strip__title { font-family: "Montserrat", sans-serif; font-weight: 700; font-size: 15px; letter-spacing: 1.5px; }
  .strip__subtitle { font-family: "Montserrat", sans-serif; font-size: 9px; letter-spacing: 1.5px; }

  .back__panel {
    position: absolute; left: 232px; top: 34px; width: 310px; height: 250px;
    background: var(--ink);
    display: flex; flex-direction: column; justify-content: space-around;
    padding: 10px 12px 10px 20px;
  }
  .back__panel-segment { position: absolute; left: 0; width: 100%; background: var(--ink-soft); }
  .contact { position: relative; display: flex; align-items: center; gap: 14px; color: var(--white); }
  .contact__icon {
    flex: none; width: 26px; height: 26px; background: var(--blue);
    display: flex; align-items: center; justify-content: center;
  }
  .contact__lines { font-size: 12px; line-height: 1.4; white-space: nowrap; }
</style>
</head>
<body>

<section class="card card--front" aria-label="Voorzijde visitekaartje">
  <div class="front__topband">
    <div class="front__topband-segment" style="left:120px;width:130px"></div>
    <div class="front__topband-segment" style="left:380px;width:90px"></div>
  </div>
  <div class="brand">
    <div class="brand__row">
      <span class="brand__mark"></span>
      <span class="brand__name">HUIDPUNTZORG</span>
    </div>
    <span class="brand__tagline">next generation skin care</span>
  </div>
  <div class="front__bottomband">
    <div class="front__bottomband-segment" style="left:150px;width:120px"></div>
    <div class="front__bottomband-segment" style="left:430px;width:70px"></div>
  </div>
</section>

<section class="card card--back" aria-label="Achterzijde visitekaartje">
  <div class="back__frame">
    <div class="back__frame-segment" style="left:0;top:0;width:52px;height:34px"></div>
    <div class="back__frame-segment" style="left:0;bottom:0;width:52px;height:36px"></div>
  </div>
  <div class="back__side">
    <div class="brand">
      <div class="brand__row">
        <span class="brand__mark"></span>
        <span class="brand__name">HUIDPUNTZORG</span>
      </div>
      <span class="brand__tagline">next generation skin care</span>
    </div>
  </div>
  <div class="back__strip">
    <div class="strip__text">
      <div class="strip__title">HUIDKLINIEK</div>
      <div class="strip__subtitle">ROTTERDAM · AMSTERDAM</div>
    </div>
  </div>
  <div class="back__panel">
    <div class="back__panel-segment" style="top:0;height:70px"></div>
    <div class="back__panel-segment" style="top:160px;height:90px"></div>

    <div class="contact">
      <span class="contact__icon">
        <svg width="14" height="14" viewBox="0 0 24 24" aria-hidden="true"><path fill="#fff" d="M6.6 10.8a15.1 15.1 0 0 0 6.6 6.6l2.2-2.2a1 1 0 0 1 1-.25 11.4 11.4 0 0 0 3.6.57 1 1 0 0 1 1 1V20a1 1 0 0 1-1 1A17 17 0 0 1 3 4a1 1 0 0 1 1-1h3.5a1 1 0 0 1 1 1c0 1.25.2 2.450.57 3.57a1 1 0 0 1-.25 1z"/></svg>
      </span>
      <div class="contact__lines">010 483 21 95<br>020 571 3829</div>
    </div>

    <div class="contact">
      <span class="contact__icon">
        <svg width="14" height="14" viewBox="0 0 24 24" aria-hidden="true"><g fill="none" stroke="#fff" stroke-width="2"><circle cx="12" cy="12" r="9"/><ellipse cx="12" cy="12" rx="4" ry="9"/><path d="M3 12h18"/></g></svg>
      </span>
      <div class="contact__lines">info@huidpuntzorg.nu<br>www.huidpuntzorg.nu</div>
    </div>

    <div class="contact">
      <span class="contact__icon">
        <svg width="14" height="14" viewBox="0 0 24 24" aria-hidden="true"><path fill="#fff" d="M12 2a7 7 0 0 0-7 7c0 5.2 7 13 7 13s7-7.8 7-13a7 7 0 0 0-7-7zm0 9.5A2.5 2.5 0 1 1 12 6.5a2.5 2.5 0 0 1 0 5z"/></svg>
      </span>
      <div class="contact__lines">Lindenhoflaan 214B, 3041KP Rotterdam<br>Zonnewijzerstraat 238, 1062RT Amsterdam</div>
    </div>
  </div>
</section>

</body>
</html>
```